Ora- luxurious rental suites coming soon

Looking for a large size banner design. The banner will include the logo "ORA". The logo has already been designed by one of your designers (Belmiro). The banner is to be placed on the building fence and will be used as a marketing/ advertisement purpose to display what's coming soon. It needs to be clean and elegant since it's representing upscale apartements.
Requesting Belmiro to be one of the designers. Thanks.
Updates

Hi all-here is the logo link. Banner will be printed on 3 separate boards that will be attached side by side to look like one big one. We are doing it this way to be able to make future modifications on 1 board at a time. Each board will be 10'Wx8'H panel. Logo design needs to be in the middle board and other left and right side boards will have the info like "coming soon and building picture". For now, please use any building image, I will be sending the actual building image later on for an update. Please do not include full image of building, choose a section and zoom or crop portion of building image so it looks more interesting. Building will be a luxurious rental in downtown. Thanks. https://www.filecrate.net/sh/k4mwpxq7r2d9vzb/QRT8LMN2K_hx_WBZcpfkeH3Lo?dl=0x

Re: banner: Instead of "coming soon" please use "coming this fall'. Thanks

Target Market(s)

professionals

Industry/Entity Type

Residential rentals

Font styles to use
Serif

Requirements
Must have
• use wording such as: coming this fall, 1&2 bedroom suites, designer finishes, terrace views
Nice to have
• Banner will be placed on site over a black mesh backdrop. Please design in a way that will make it look like blending with mesh
Should not have
• Banner should not be too colorf. Please use white, grey or yellow... refer to logo image

```html
<!DOCTYPE html>
<html lang="en">
<head>
<meta charset="utf-8">
<title>Ora – Fence Banner</title>
<link rel="stylesheet" href="https://fonts.googleapis.com/css2?family=Nunito+Sans:wght@300;400&family=PT+Sans&family=Montserrat:wght@500&display=swap">
<style>
  :root {
    --backdrop: #404042;
    --paper: #ffffff;
    --sage: #727d72;
    --ink: #3a3a3a;
    --yellow: #ffd000;
    --veil: rgba(250, 250, 250, 0.9);
    --muted: #6c6c6c;
  }
  * { margin: 0; padding: 0; box-sizing: border-box; }
  html, body {
    width: 1200px;
    height: 1000px;
    overflow: hidden;
    background: var(--backdrop);
  }
  .canvas {
    position: relative;
    width: 1200px;
    height: 1000px;
  }
  .banner {
    position: absolute;
    left: 86px;
    top: 363px;
    width: 1028px;
    height: 274px;
    display: flex;
  }
  .board {
    position: relative;
    width: 342.67px;
    height: 100%;
    overflow: hidden;
  }
  .board-left .building-photo {
    position: absolute;
    inset: 0;
    background: linear-gradient(100deg, #d9c8a2 0%, #e9dcc0 35%, #e3e6ea 60%, #d4e0f5 80%, #d3e0f7 100%);
  }
  .headline-box {
    position: absolute;
    left: 0;
    top: 66px;
    width: 190px;
    height: 143px;
    background: var(--veil);
  }
  .headline {
    position: absolute;
    left: 27px;
    top: 22px;
    font-family: "Nunito Sans", sans-serif;
    font-weight: 300;
    font-size: 40px;
    line-height: 48px;
    color: var(--sage);
    letter-spacing: 0.2px;
  }
  .board-center {
    background: var(--paper);
  }
  .brand {
    position: absolute;
    left: 0;
    right: 0;
    top: 104px;
    text-align: center;
  }
  .brand-address {
    font-family: "Montserrat", sans-serif;
    font-weight: 500;
    font-size: 7.5px;
    letter-spacing: 2px;
    color: var(--muted);
    margin-left: 50px;
  }
  .brand-name {
    font-family: "Nunito Sans", sans-serif;
    font-weight: 300;
    font-size: 60px;
    line-height: 60px;
    letter-spacing: 2px;
    color: var(--sage);
  }
  .board-right .suite-photo {
    position: absolute;
    left: 0;
    top: 0;
    width: 100%;
    height: 223px;
    background: linear-gradient(180deg, #ede3d8 0%, #e6d6c3 45%, #efebe6 70%, #cfcac4 100%);
  }
  .feature-band {
    position: absolute;
    left: 0;
    bottom: 0;
    width: 100%;
    height: 51px;
    background: var(--yellow);
    display: flex;
    align-items: center;
    justify-content: center;
  }
  .feature-text {
    font-family: "PT Sans", sans-serif;
    font-size: 17px;
    color: var(--ink);
    white-space: pre;
  }
  .page-number {
    position: absolute;
    right: 10px;
    bottom: 7px;
    font-family: "PT Sans", sans-serif;
    font-size: 11px;
    color: #ffffff;
  }
</style>
</head>
<body>
<div class="canvas">
  <div class="banner">
    <section class="board board-left">
      <div class="building-photo" role="img" aria-label="Close-up of cream balconies with glass railings against a pale blue sky"></div>
      <div class="headline-box">
        <p class="headline">on the<br>horizon</p>
      </div>
    </section>
    <section class="board board-center">
      <div class="brand">
        <p class="brand-address">415 LINDELL</p>
        <p class="brand-name">ORA</p>
      </div>
    </section>
    <section class="board board-right">
      <div class="suite-photo" role="img" aria-label="Bright bedroom suite with upholstered headboard, bench and sheer curtains"></div>
      <div class="feature-band">
        <p class="feature-text">1&amp;2 bedroom suites,  designer finishes</p>
      </div>
    </section>
  </div>
  <span class="page-number">002</span>
</div>
</body>
</html>
```